On going F&B business needs a new stationery design for festive occasion

Would like something like the attached file, but with a new look. The basis colours should still be green and yellow.

```html
<!DOCTYPE html>
<html lang="en">
<head>
<meta charset="utf-8">
<title>Al - Bayan Eating Corner — Business Card</title>
<link href="https://fonts.googleapis.com/css2?family=Montserrat:wght@400;600&display=swap" rel="stylesheet">
<style>
  :root {
    --stage: #9e9e9e;
    --stage-dark: #6e6e6e;
    --lime: #a9d23a;
    --green: #5db33f;
    --forest: #2f8a3e;
    --white: #ffffff;
    --ink: #2b2b2b;
    --rule: #3c9440;
  }
  * { box-sizing: border-box; margin: 0; padding: 0; }
  html, body {
    width: 1089px; height: 1200px; overflow: hidden;
  }
  body {
    background: linear-gradient(90deg, var(--stage-dark), var(--stage));
    font-family: "Montserrat", sans-serif;
    position: relative;
  }
  .card {
    position: absolute;
    left: 94px;
    width: 900px;
    height: 515px;
    box-shadow: 0 6px 18px rgba(0,0,0,.35);
    overflow: hidden;
  }
  .card--front { top: 60px; }
  .card--back { top: 625px; background: var(--white); display: flex; }

  .green-field {
    background: linear-gradient(180deg, var(--lime) 0%, var(--green) 50%, var(--forest) 100%);
  }
  .card--front .green-field {
    position: absolute; inset: 0;
  }
  .brand {
    position: absolute;
    display: flex;
    align-items: center;
    color: var(--white);
    font-weight: 600;
    text-transform: uppercase;
  }
  .brand__dot {
    border: 6px solid var(--white);
    border-radius: 50%;
    flex: none;
  }
  .card--front .brand {
    left: 110px; top: 160px; gap: 36px;
  }
  .card--front .brand__dot { width: 170px; height: 170px; }
  .card--front .brand__name { font-size: 62px; line-height: 1.1; letter-spacing: 2px; }
  .card--front .brand__name span { display: block; font-size: 40px; letter-spacing: 3px; margin-left: 36px; }

  .card--back .green-field {
    position: relative;
    width: 330px; height: 100%;
    box-shadow: 4px 0 10px rgba(0,0,0,.18);
  }
  .card--back .brand {
    left: 16px; top: 216px; gap: 14px;
  }
  .card--back .brand__dot { width: 74px; height: 74px; border-width: 3px; }
  .card--back .brand__name { font-size: 27px; line-height: 1.15; letter-spacing: 1px; }
  .card--back .brand__name span { display: block; font-size: 18px; letter-spacing: 1.5px; margin-left: 14px; }

  .contact {
    list-style: none;
    margin: 150px 0 0 42px;
    padding-left: 26px;
    border-left: 2px solid var(--rule);
    align-self: flex-start;
    color: var(--ink);
    font-size: 19px;
    line-height: 1.4;
  }
  .contact li {
    display: flex; align-items: flex-start; gap: 12px;
    margin-bottom: 18px;
  }
  .contact li:last-child { margin-bottom: 0; }
  .contact__icon { width: 38px; height: 38px; flex: none; }
</style>
</head>
<body>

<section class="card card--front" aria-label="Card front">
  <div class="green-field" role="img" aria-label="Green-to-lime gradient with faint festive lanterns and mosque silhouettes"></div>
  <div class="brand">
    <div class="brand__dot"></div>
    <p class="brand__name">Al - Bayan<span>Eating Corner</span></p>
  </div>
</section>

<section class="card card--back" aria-label="Card back">
  <div class="green-field" role="img" aria-label="Green-to-lime gradient with faint festive lanterns and mosque silhouettes">
    <div class="brand">
      <div class="brand__dot"></div>
      <p class="brand__name">Al - Bayan<span>Eating Corner</span></p>
    </div>
  </div>

  <svg width="0" height="0" style="position:absolute" aria-hidden="true">
    <defs>
      <linearGradient id="icon-fill" x1="0" y1="0" x2="0" y2="1">
        <stop offset="0" stop-color="#a9d23a"/>
        <stop offset="1" stop-color="#2f8a3e"/>
      </linearGradient>
    </defs>
  </svg>

  <ul class="contact">
    <li>
      <svg class="contact__icon" viewBox="0 0 38 38" aria-hidden="true">
        <circle cx="19" cy="19" r="19" fill="url(#icon-fill)"/>
        <path d="M19 8a8 8 0 0 0-8 8c0 6 8 14 8 14s8-8 8-14a8 8 0 0 0-8-8z" fill="#fff"/>
        <circle cx="19" cy="16" r="3" fill="#3c9440"/>
      </svg>
      <span>12, Kranji Park Way #02-08<br>Singapore 730412</span>
    </li>
    <li>
      <svg class="contact__icon" viewBox="0 0 38 38" aria-hidden="true">
        <circle cx="19" cy="19" r="19" fill="url(#icon-fill)"/>
        <path d="M13 10l4 0 2 5-3 2c1 3 3 5 6 6l2-3 5 2v4c0 1-1 2-2 2-9 0-16-7-16-16 0-1 1-2 2-2z" fill="#fff"/>
      </svg>
      <span>6412 3087</span>
    </li>
    <li>
      <svg class="contact__icon" viewBox="0 0 38 38" aria-hidden="true">
        <circle cx="19" cy="19" r="19" fill="url(#icon-fill)"/>
        <rect x="10" y="12" width="6" height="16" rx="1.5" fill="#fff"/>
        <rect x="17" y="12" width="12" height="16" rx="1.5" fill="#fff"/>
        <rect x="19" y="14" width="8" height="4" fill="#3c9440"/>
        <rect x="19" y="20" width="2" height="2" fill="#3c9440"/>
        <rect x="22" y="20" width="2" height="2" fill="#3c9440"/>
        <rect x="25" y="20" width="2" height="2" fill="#3c9440"/>
        <rect x="19" y="23" width="2" height="2" fill="#3c9440"/>
        <rect x="22" y="23" width="2" height="2" fill="#3c9440"/>
        <rect x="25" y="23" width="2" height="2" fill="#3c9440"/>
      </svg>
      <span>6412 3087</span>
    </li>
    <li>
      <svg class="contact__icon" viewBox="0 0 38 38" aria-hidden="true">
        <circle cx="19" cy="19" r="19" fill="url(#icon-fill)"/>
        <rect x="9" y="12" width="20" height="14" rx="1.5" fill="#fff"/>
        <path d="M9.5 13l9.5 7 9.5-7M9.5 25.5l7-6M28.5 25.5l-7-6" fill="none" stroke="#3c9440" stroke-width="1.5"/>
      </svg>
      <span>hello@albayan-eats.sg</span>
    </li>
  </ul>
</section>

</body>
</html>
```